Home Refinance . Residential Mortgages

I want to post a small flyer as part of an email. I want do an email blast. I am a mortgage company and want to entice borrowers with my low interest rates. My website is www.brookmerelending.com
The colors must match the website colors.
QT BRSL REFINANCE.
30 YR. FIXED RATES as low as
2.25% | 2.437% APR
No Appraisal, No out of Pocket cost, NO Income Verification, NO Asset Verification, Close in 30 days or less

Target Market(s)

Real Estate agents & Borrowers looking to get a mortgage loan

Colors
0455a3
ec1f27
28a1d5

Requirements
Must have
• The colors must match the website colors.
BROOKMERE LENDING, INC,.
4817B Halloway Road
Alexandria, VA 58147
RLCB 5830276
www.rlcbborrowerlookup.com

Open Keystone Allegiance LOGO.

```html
<!DOCTYPE html>
<html lang="en">
<head>
<meta charset="utf-8">
<title>Brookmere Lending – QT BRSL Refinance</title>
<link href="https://fonts.googleapis.com/css2?family=Bebas+Neue&family=Open+Sans:wght@400;700&display=swap" rel="stylesheet">
<style>
  :root {
    --brand-blue: #0455a3;
    --royal-blue: #0b2fe0;
    --deep-blue: #0a1fb8;
    --sky-blue: #28a1d5;
    --cyan: #56d4f6;
    --rate-red: #ec1f27;
    --ink: #1d1d1f;
    --white: #ffffff;
  }
  html, body { margin: 0; padding: 0; overflow: hidden; background: #ffffff; }
  .flyer {
    position: relative; width: 848px; height: 1200px; overflow: hidden;
    background: var(--white); font-family: "Bebas Neue", sans-serif;
  }
  .flyer-shapes { position: absolute; inset: 0; }
  .brand {
    position: absolute; left: 478px; top: 52px;
    display: flex; align-items: center; gap: 10px;
    font-family: "Open Sans", sans-serif; font-weight: 400;
    font-size: 28px; line-height: 1; color: var(--ink); white-space: nowrap;
  }
  .brand-mark { width: 38px; height: 38px; background: var(--brand-blue); flex: none; }
  .benefits { position: absolute; left: 122px; top: 548px; margin: 0; padding: 0; list-style: none; }
  .benefits li {
    display: flex; align-items: center; height: 58.6px;
    font-size: 55px; color: var(--royal-blue); line-height: 1;
  }
  .benefits .dot {
    width: 32px; height: 32px; border-radius: 50%; margin-right: 26px; flex: none;
    background: radial-gradient(circle at 40% 35%, #7fd0ff, var(--royal-blue) 70%);
    display: flex; align-items: center; justify-content: center;
  }
  .benefits .dot::after { content: ""; width: 8px; height: 12px; border-radius: 4px 4px 2px 2px; background: var(--white); }
  .closing { position: absolute; left: 113px; top: 828px; color: var(--royal-blue); line-height: 1; }
  .closing-lead, .closing-tail { font-size: 46px; }
  .closing-days { font-size: 104px; color: var(--rate-red); letter-spacing: -1px; margin: 2px 0 -2px; }
  .rate-offer {
    position: absolute; left: 440px; top: 872px; width: 360px;
    text-align: center; color: var(--white); line-height: 1;
  }
  .rate-offer p { margin: 0; font-size: 36px; white-space: nowrap; }
  .rate-offer .rate-figures { color: var(--rate-red); font-size: 56px; margin-top: 4px; }
  .rate-figures small { font-size: 34px; }
  .company-info {
    position: absolute; left: 240px; top: 1080px; width: 400px; text-align: center;
    font-family: "Open Sans", sans-serif; font-weight: 700; font-size: 18.5px;
    line-height: 24.8px; color: var(--white);
  }
  .company-info p { margin: 0; white-space: nowrap; }
  .housing-badge {
    position: absolute; left: 695px; top: 1082px; width: 95px; height: 94px;
    border-radius: 8px; background: var(--white); border: 2px solid var(--deep-blue);
    box-sizing: border-box; display: flex; align-items: center; justify-content: center;
  }
  .housing-badge span { width: 58px; height: 44px; background: var(--brand-blue); }
</style>
</head>
<body>
<main class="flyer">
  <svg class="flyer-shapes" width="848" height="1200" viewBox="0 0 848 1200">
    <defs>
      <linearGradient id="photoTones" x1="0" y1="0" x2="0" y2="1">
        <stop offset="0" stop-color="#a9d4ec"/>
        <stop offset="1" stop-color="#86cbd8"/>
      </linearGradient>
      <linearGradient id="cornerBlue" x1="0" y1="0" x2="1" y2="0.6">
        <stop offset="0" stop-color="#0b1fe0"/>
        <stop offset="1" stop-color="#3fb8f5"/>
      </linearGradient>
      <linearGradient id="bandBlue" x1="0" y1="0" x2="1" y2="0">
        <stop offset="0" stop-color="#0a1ab0"/>
        <stop offset="1" stop-color="#1f5ce8"/>
      </linearGradient>
      <linearGradient id="diamondBlue" x1="0" y1="1" x2="1" y2="0">
        <stop offset="0" stop-color="#1030e0"/>
        <stop offset="1" stop-color="#4cc0f5"/>
      </linearGradient>
      <linearGradient id="rateBand" x1="0" y1="0" x2="0" y2="1">
        <stop offset="0" stop-color="#0b2fe0"/>
        <stop offset="1" stop-color="#4fd0f6"/>
      </linearGradient>
      <linearGradient id="footerBand" x1="0" y1="0" x2="1" y2="1">
        <stop offset="0" stop-color="#55d6f7"/>
        <stop offset="1" stop-color="#1840e6"/>
      </linearGradient>
      <linearGradient id="greyFade" x1="0" y1="0" x2="1" y2="0">
        <stop offset="0" stop-color="#d9d9d9"/>
        <stop offset="1" stop-color="#ffffff"/>
      </linearGradient>
    </defs>

    <rect role="img" aria-label="Photo of a white pool house with a backyard swimming pool" x="0" y="0" width="848" height="680" fill="url(#photoTones)"/>

    <polygon points="0,0 555,0 120,250 0,330" fill="url(#cornerBlue)"/>
    <polygon points="0,175 80,215 300,380 225,410 0,285" fill="url(#bandBlue)"/>
    <polygon points="0,285 120,350 180,390 40,415 0,400" fill="#2a5cf0"/>
    <polygon points="0,395 170,370 60,400 0,430" fill="#5ac8f5"/>
    <polygon points="0,430 145,400 35,480 0,500" fill="#ffffff" opacity="0.9"/>
    <polygon points="17,420 150,400 17,520" fill="url(#greyFade)"/>
    <polygon points="0,400 17,390 17,1011 0,1011" fill="#56d4f6"/>

    <polygon points="17,529 120,455 358,335 848,666 828,666 828,1058 17,1058" fill="#ffffff"/>
    <polygon points="105,460 350,335 420,365 190,528" fill="url(#diamondBlue)"/>
    <polygon points="105,460 190,528 220,505 150,455" fill="#0a1ab0" opacity="0.6"/>
    <polygon points="828,666 848,660 848,1058 828,1058" fill="#56d4f6"/>

    <polygon points="475,851 848,851 848,1016 375,1016" fill="url(#rateBand)"/>

    <rect x="0" y="1058" width="848" height="142" fill="url(#footerBand)"/>
    <polygon points="0,1011 17,1011 220,1200 0,1200" fill="#6fd8f8"/>
    <polygon points="0,1011 199,1200 0,1200" fill="#0a1ab0"/>
  </svg>

  <div class="brand"><span class="brand-mark"></span>Brookmere Lending</div>

  <ul class="benefits">
    <li><span class="dot"></span>No Appraisal</li>
    <li><span class="dot"></span>No Out of Pocket Cost</li>
    <li><span class="dot"></span>No Income Verification</li>
    <li><span class="dot"></span>No Asset Verification</li>
  </ul>

  <div class="closing">
    <div class="closing-lead">Close in</div>
    <div class="closing-days">30 Days</div>
    <div class="closing-tail">or less</div>
  </div>

  <div class="rate-offer">
    <p>QT BRSL Refinance.</p>
    <p>30 Yr. Fixed Rates as low as</p>
    <p class="rate-figures">2.25% | 2.437% <small>APR</small></p>
  </div>

  <div class="company-info">
    <p>BROOKMERE LENDING, INC,.</p>
    <p>4817B Halloway Road Alexandria, VA 58147</p>
    <p>RLCB 5830276</p>
    <p>www.rlcbborrowerlookup.com</p>
  </div>

  <div class="housing-badge" role="img" aria-label="Open Keystone Allegiance badge"><span></span></div>
</main>
</body>
</html>
```